I am writing a book called "SMILING OPENS EVERY DOOR "

I NEED A BOOK COVER FOR MY BOOK" SMILING OPENS EVERY DOOR"
so So Who Is Knocking? " ( this in smaller font)

"Smiling Opens Every Door " will need to designed to eventually be a logo , banner and business card
COLOURS MAINLY ORANGE AND WHITE (with accents bright colour )

THE BOOK IS MY LAUGHTER JOURNEY AS A PERFORMER AND ADVENTURE INDIA LEARNING ABOUT LAUGHTER YOGA WHICH I WILL BE TEACHING

I do not want photos on the front cover ..
The look could be modern and eye-catching
I have also just been to India to learn Laughing Yoga with Dr Tobin Verhaal

Thank-you so much everyone for your brilliant designs . i am overwhelmed with your talent . i hope to work with you all again soon ! Marnie  

Target Market(s)

"Adults based in western speaking countries aged 25 to 60 that want to learn to laugh more
Also this book will be sold at my conference workshops

Industry/Entity Type

Business

Requirements
Must have
• ORANGE AND WHITE
CAN HAVE AQUA , HOT PINK , LIME GREEN, YELLOW ACCENTS

THESE WILL BE DIFFERENT AREAS WILL COVERING IN MY BOOK
EG LAUGHTER NAD BREAT CANCER ( PINK)
LAUGHTER NAD DEPRESSION ( BLUE)
LAUGHTER AND KIDS ( YELLOW)

NO Photos on front cover
Should not have
• No photos

```html
<!DOCTYPE html>
<html lang="en">
<head>
<meta charset="utf-8">
<title>Smiling Opens Every Door – Book Cover</title>
<link href="https://fonts.googleapis.com/css2?family=Arimo:wght@700&display=swap" rel="stylesheet">
<style>
  :root {
    --page-bg: #ffffff;
    --cover-bg: #ffffff;
    --cover-edge: #e4e6e6;
    --orange-light: #fbc531;
    --orange-deep: #e9a010;
    --orange-text: #efab1b;
    --white: #ffffff;
  }
  html, body {
    margin: 0;
    padding: 0;
    width: 1200px;
    height: 1000px;
    overflow: hidden;
    background: var(--page-bg);
  }
  .canvas {
    position: relative;
    width: 1200px;
    height: 1000px;
  }
  .book-cover {
    position: absolute;
    left: 300px;
    top: 50px;
    width: 600px;
    height: 900px;
    box-shadow: 0 10px 30px rgba(0, 0, 0, 0.12);
  }
  .book-cover svg {
    display: block;
    width: 600px;
    height: 900px;
  }
  .cover-type {
    font-family: "Arimo", Arial, sans-serif;
    font-weight: 700;
  }
  .title-word { fill: var(--orange-text); }
  .subtitle { fill: var(--white); }
  .author { fill: var(--orange-text); }
</style>
</head>
<body>
<main class="canvas">
  <div class="book-cover">
    <svg viewBox="0 0 600 900" xmlns="http://www.w3.org/2000/svg" aria-labelledby="cover-title">
      <title id="cover-title">Smiling Opens Every Door – So Who Is Knocking? by Marnie Pennick</title>
      <defs>
        <linearGradient id="orange-fill" x1="0" y1="0" x2="1" y2="1">
          <stop offset="0" stop-color="var(--orange-light)"/>
          <stop offset="1" stop-color="var(--orange-deep)"/>
        </linearGradient>
      </defs>

      <rect class="cover-surface" x="0" y="0" width="600" height="900" fill="var(--cover-bg)" stroke="var(--cover-edge)" stroke-width="1"/>

      <g class="title-block">
        <text class="cover-type title-word title-line-1" x="30" y="150" font-size="120">SMILING</text>
        <text class="cover-type title-word title-line-2" x="30" y="300" font-size="140">OPENS</text>
        <text class="cover-type title-word title-line-3" x="30" y="450" font-size="140">EVERY</text>
        <text class="cover-type title-word title-line-4" x="30" y="600" font-size="140">DOOR</text>
      </g>

      <rect class="subtitle-band" x="30" y="650" width="540" height="120" fill="url(#orange-fill)"/>
      <text class="cover-type subtitle" x="300" y="725" font-size="42" text-anchor="middle">So Who Is Knocking?</text>

      <text class="cover-type author" x="570" y="835" font-size="34" text-anchor="end">by Marnie Pennick</text>
    </svg>
  </div>
</main>
</body>
</html>
```